Brass Lantern Video Solutions Brochure

We need a DOUBLE GATE FOLD 4 PANEL brochure for our video production company. The brochure will show pics of our green screen studio, some post production images "like the weatherman" standing in front of a weather map, and descriptions of our services and pricing. I really want this to look professional and classy. I will upload photos I want to use.

Target Market(s)

The main target of our company is physicians and other medical professionals. More men than women.

Industry/Entity Type

It Company

Font styles to use
Serif
Sans Serif

Requirements
Must have
• Professional, high end.
Colors - the logo is on black. I would try to make the brochure black so the colors and images pop off the page. Our colors are blue and white as in the logo.
Nice to have
• It should be able to be mailed so the ouside back should be white with a place for a label to be attached.

```html
<!DOCTYPE html>
<html lang="en">
<head>
<meta charset="utf-8">
<title>Brass Lantern Video Solutions – Tri-fold Brochure</title>
<link rel="stylesheet" href="https://fonts.googleapis.com/css2?family=Open+Sans:ital,wght@0,400;0,600;0,700;1,400;1,600;1,700&display=swap">
<style>
:root{
  --page:#e4e4e4;
  --ink:#0c0c0c;
  --blue:#1ea0d8;
  --blue-deep:#0b6f9e;
  --blue-soft:#5cc3ee;
  --white:#ffffff;
  --ribbon:#e6e7e9;
  --mist:#d9dadc;
  --copy:#f1f1f1;
}
*{box-sizing:border-box;margin:0;padding:0}
html,body{width:982px;height:1200px;overflow:hidden}
body{background:var(--page);font-family:"Open Sans",Arial,sans-serif;position:relative}
.sheet{position:absolute;left:57.6px;width:876px;height:530px;background:var(--ink);overflow:hidden;box-shadow:0 2px 6px rgba(0,0,0,.18)}
.sheet--outside{top:45.6px}
.sheet--inside{top:621.6px}
.panel{position:absolute;top:0;height:530px;overflow:hidden}
.abs{position:absolute}
.photo{position:absolute}
.lorem{color:var(--copy);font-size:9.4px;line-height:1.28;text-align:justify}

/* outside – panel 1 */
.back-cover{left:0;width:219px;background:var(--ink)}
.cover-sky{left:0;top:0;width:219px;height:124px;background:linear-gradient(135deg,#1690c4 0%,#27a7dd 55%,#1584b8 100%)}
.cover-band{left:0;top:124px;width:219px;height:20px;background:var(--white)}
.call-label{top:22px;width:219px;text-align:center;color:var(--white);font-size:17px;font-weight:600}
.call-number{top:48px;width:219px;text-align:center;color:var(--white);font-size:24px;font-weight:600;letter-spacing:.3px}
.visit-label{top:443px;width:219px;text-align:center;color:var(--white);font-size:10.5px;font-weight:700;font-style:italic}
.visit-url{top:462px;width:219px;text-align:center;color:var(--white);font-size:13.5px;font-weight:600;white-space:nowrap}

/* outside – panel 2 mailer */
.mailer{left:219px;width:219px;background:linear-gradient(160deg,#fbfbfb 0%,#e9eaec 45%,#cfd1d4 70%,#f2f2f2 100%)}
.stamp{left:11px;top:12px;width:76px;height:82px;border:1px solid #555;background:var(--white)}
.address-line{top:12px;width:1px;height:188px;background:#555}
.contact{position:absolute;left:14px;top:522px;width:250px;height:156px;transform-origin:0 0;transform:rotate(-90deg)}
.contact p{position:absolute;left:0;white-space:nowrap}
.contact-title{color:var(--blue);font-size:17px;font-weight:700;line-height:22px;left:0}
.contact-line{color:#2a2a2a;font-size:10.5px;line-height:14px;display:flex;align-items:flex-start;gap:9px}
.contact-line svg{width:11px;height:11px;flex:none;margin-top:1.5px}

/* outside – panel 3 services */
.services{left:438px;width:219px;background:var(--ink)}
.services-title{top:25px;width:219px;text-align:center;color:var(--white);font-size:12.5px;font-weight:700;font-style:italic}
.service{left:23px;width:183px;height:36px}
.service-num{position:absolute;left:0;top:0;width:33px;height:36px;background:var(--blue);color:var(--white);font-weight:700;font-size:15px;display:flex;align-items:center;justify-content:center}
.service-num::after{content:"";position:absolute;right:-8px;top:10px;border-left:8px solid var(--blue);border-top:8px solid transparent;border-bottom:8px solid transparent}
.service-ribbon{position:absolute;left:33px;top:0;width:150px;height:36px;background:var(--ribbon);clip-path:polygon(0 0,100% 0,88% 50%,100% 100%,0 100%);padding-left:21px;display:flex;align-items:center;color:#111;font-weight:700;font-size:13.5px}
.services-copy{left:23px;top:431px;width:183px}

/* outside – panel 4 cover */
.front-cover{left:657px;width:219px;background:var(--ink)}
.front-sky{left:0;top:0;width:219px;height:124px;background:linear-gradient(135deg,#1584b8 0%,#2aa9df 50%,#1488bd 100%)}
.front-band{left:0;top:124px;width:219px;height:20px;background:var(--white)}
.tagline{top:14px;width:219px;text-align:center;color:var(--white);font-style:italic;font-weight:600;line-height:1.2}
.tagline span{display:block}
.tagline .lead{font-size:15.5px}
.tagline .big{font-size:24px;font-weight:700}
.tagline .tail{font-size:15.5px}
.brand{top:452px;width:219px;text-align:center;color:var(--blue);font-size:19px;font-weight:600;line-height:1.15}
.brand-dot{left:98px;top:418px;width:24px;height:24px;border-radius:50%;background:var(--white)}

/* inside */
.who{left:0;width:216px;background:var(--ink);padding:0 14px}
.heading-blue{color:var(--blue);font-size:18px;font-weight:400}
.who-title{top:17px;left:14px}
.who-copy{left:14px;width:188px}
.who-accent{color:var(--blue);font-style:italic}
.what{left:216px;width:444px;background:var(--blue)}
.what-title{left:12px;top:13px;color:var(--white);font-size:22px}
.what-intro{left:12px;top:47px;width:420px;color:var(--white)}
.card{width:184px}
.card-title{display:flex;align-items:center;gap:8px;color:var(--white);font-size:14px;font-weight:600}
.card-title i{display:block;width:14px;height:14px;border-radius:50%;background:var(--white)}
.card-photo{margin-top:8px;height:79px}
.card-copy{margin-top:7px;color:var(--white)}
.divider-v{left:219px;top:110px;width:1px;height:398px;background:rgba(255,255,255,.55)}
.divider-h{left:18px;top:302px;width:408px;height:1px;background:rgba(255,255,255,.55)}
.play{left:208px;top:290px;width:24px;height:24px}
.why{left:660px;width:216px;background:var(--ink)}
.why-title{left:12px;top:240px;font-size:17px}
.why-copy{left:12px;width:192px}
</style>
</head>
<body>

<section class="sheet sheet--outside">
  <div class="panel back-cover">
    <div class="abs cover-sky"></div>
    <p class="abs call-label">Call Us Today</p>
    <p class="abs call-number">555 014 2870</p>
    <div class="abs cover-band"></div>
    <div class="photo" style="left:0;top:144px;width:219px;height:228px;background:linear-gradient(160deg,#2d3f7a 0%,#6b7fc2 35%,#a9c7ea 65%,#3f6aa6 100%)" role="img" aria-label="Film strip of city night scenes sweeping across a blue background"></div>
    <svg class="abs" style="left:0;top:372px" width="219" height="70" viewBox="0 0 219 70" aria-hidden="true">
      <polygon points="0,0 30,0 14,70 0,70" fill="var(--blue)"/>
      <polygon points="0,0 18,0 0,50" fill="var(--white)"/>
    </svg>
    <p class="abs visit-label">For more information Visit</p>
    <p class="abs visit-url">www.brasslanternvideo.com</p>
  </div>

  <div class="panel mailer">
    <div class="photo" style="left:0;top:0;width:219px;height:530px;opacity:.35;background:radial-gradient(circle at 110px 330px,#8d9095 0%,#c8cacd 35%,transparent 70%)" role="img" aria-label="Faded close-up of a camera lens"></div>
    <div class="abs stamp"></div>
    <div class="abs address-line" style="left:134px"></div>
    <div class="abs address-line" style="left:170px"></div>
    <div class="abs address-line" style="left:204px"></div>
    <div class="contact">
      <p class="contact-title" style="top:1px">Contact Info</p>
      <p class="contact-line" style="top:38px"><svg viewBox="0 0 12 12"><path d="M6 1a3.5 3.5 0 0 0-3.5 3.5C2.5 7.5 6 11 6 11s3.5-3.5 3.5-6.5A3.5 3.5 0 0 0 6 1zm0 5a1.4 1.4 0 1 1 0-2.8A1.4 1.4 0 0 1 6 6z" fill="#333"/></svg><span>1480 Harbor Lane Millbrook,<br>AL(Alabama) 35054</span></p>
      <p class="contact-line" style="top:83px"><svg viewBox="0 0 12 12"><path d="M3 1h2l1 3-1.5 1a6 6 0 0 0 2.5 2.5L8 6l3 1v2a1.5 1.5 0 0 1-1.5 1.5A8.5 8.5 0 0 1 1.5 2.5 1.5 1.5 0 0 1 3 1z" fill="#333"/></svg>(205) 555-0147</p>
      <p class="contact-line" style="top:110px"><svg viewBox="0 0 12 12"><rect x="1" y="2.5" width="10" height="7" fill="#333"/><path d="M1 2.5l5 4 5-4" stroke="#fff" fill="none"/></svg>info@brasslantern.com</p>
      <p class="contact-line" style="top:136px"><svg viewBox="0 0 12 12"><circle cx="6" cy="6" r="4.8" stroke="#333" fill="none"/><path d="M1.2 6h9.6M6 1.2c-2.4 2.8-2.4 6.8 0 9.6M6 1.2c2.4 2.8 2.4 6.8 0 9.6" stroke="#333" fill="none"/></svg>www.brasslantern.com</p>
    </div>
  </div>

  <div class="panel services">
    <p class="abs services-title">We Provide Following Videos</p>
    <div class="abs service" style="top:70px"><span class="service-num">1</span><span class="service-ribbon">Commercial</span></div>
    <div class="abs service" style="top:130px"><span class="service-num">2</span><span class="service-ribbon">Animated</span></div>
    <div class="abs service" style="top:190px"><span class="service-num">3</span><span class="service-ribbon">Charity</span></div>
    <div class="abs service" style="top:248px"><span class="service-num">4</span><span class="service-ribbon">Corporate</span></div>
    <div class="abs service" style="top:306px"><span class="service-num">5</span><span class="service-ribbon">Promotional</span></div>
    <div class="abs service" style="top:365px"><span class="service-num">6</span><span class="service-ribbon">Medical</span></div>
    <p class="abs lorem services-copy">Lorem ipsum dolor sit amet, consectetuer adipiscing elit, sed diam nonummy nibh euismod tincidunt ut laoreet dolore magna aliquam erat volutpat. Ut wisi enim ad minim veniam, quis nostrud exerci tation ullamcorp.</p>
  </div>

  <div class="panel front-cover">
    <div class="abs front-sky"></div>
    <p class="abs tagline"><span class="lead">Make your</span><span class="big">Videos Stand out</span><span class="tail">from the crowd</span></p>
    <div class="abs front-band"></div>
    <svg class="abs" style="left:0;top:144px" width="219" height="30" viewBox="0 0 219 30" aria-hidden="true"><polygon points="0,0 219,0 219,8 0,30" fill="var(--white)"/></svg>
    <div class="photo" style="left:0;top:168px;width:219px;height:204px;background:linear-gradient(165deg,#5fb6e6 0%,#2f6fb5 40%,#1c2f6a 75%,#3a2f5a 100%)" role="img" aria-label="Film strip of colourful video stills curving over a blue light background"></div>
    <svg class="abs" style="left:189px;top:372px" width="30" height="70" viewBox="0 0 30 70" aria-hidden="true"><polygon points="16,0 30,0 30,70" fill="var(--blue)"/></svg>
    <div class="abs brand-dot"></div>
    <p class="abs brand">Brass Lantern<br>Video Solutions</p>
  </div>
</section>

<section class="sheet sheet--inside">
  <div class="panel who">
    <h2 class="abs heading-blue who-title">Who we are?</h2>
    <p class="abs lorem who-copy" style="top:50px">Lorem ipsum dolor sit amet, consectetuer adipiscing elit, sed diam nonummy nibh euismod tincidunt ut laoreet dolore magna aliquam erat volutpat. Ut wisi enim ad minim veniam, quis nostrud exerci tation ullamcorper suscipit lobortis nisl ut aliquip ex ea commodo consequat.</p>
    <p class="abs lorem who-copy who-accent" style="top:138px">Duis autem vel eum iriure dolor in hendrerit in vulputate velit esse molestie consequat, vel illum dolore eu feugiat nulla facilisis at vero eros et accumsan et iusto odio dignissim nulla facilisi.</p>
    <p class="abs lorem who-copy" style="top:214px">Lorem ipsum dolor sit amet, consectetuer adipiscing elit, sed diam nonummy nibh euismod tincidunt ut laoreet dolore magna aliquam erat volutpat. Ut wisi enim ad minim veniam, quis nostrud exerci tation ullamcorper suscipit lobortis­praesent luptatum zzril delenit augue duis dolore te feugait nulla facilisi.</p>
    <div class="photo" style="left:14px;top:335px;width:185px;height:179px;background:linear-gradient(135deg,#1d1d1d 0%,#3a3a3a 40%,#4f9e3c 70%,#2c6a22 100%)" role="img" aria-label="Video camera filming in a green screen studio"></div>
  </div>

  <div class="panel what">
    <h2 class="abs heading-blue what-title">What we do?</h2>
    <p class="abs lorem what-intro">Lorem ipsum dolor sit amet, consectetuer adipiscing elit, sed diam nonummy nibh euismod tincidunt ut laoreet dolore magna aliquam erat volutpat. Ut wisi enim ad minim veniam, quis nostrud exerci tation ullamcorper suscipit lobortispraesent luptatum zzril delenit augue duis dolore te feugait nulla facilisi.</p>

    <div class="abs divider-v"></div>
    <div class="abs divider-h"></div>
    <svg class="abs play" viewBox="0 0 24 24" aria-hidden="true"><circle cx="12" cy="12" r="12" fill="var(--white)"/><polygon points="9.5,7 17,12 9.5,17" fill="var(--blue)"/></svg>

    <article class="abs card" style="left:18px;top:117px">
      <h3 class="card-title"><i></i>Corporate Video</h3>
      <div class="photo card-photo" style="position:relative;background:linear-gradient(135deg,#eef3f8 0%,#9ec3e6 50%,#3c7fc0 100%)" role="img" aria-label="Hand touching a screen of medical icons"></div>
      <p class="lorem card-copy">Lorem ipsum dolor sit amet, consec­tetuer adipiscing elit, sed diam non­ummy nibh euismod tincidunt ut laoreet dolore magna aliquam erat volutpat.duis dolore te feugait nulla facilisi.</p>
    </article>
    <article class="abs card" style="left:242px;top:117px">
      <h3 class="card-title"><i></i>Commercial Video</h3>
      <div class="photo card-photo" style="position:relative;background:linear-gradient(180deg,#a8d2ef 0%,#cfe6f5 60%,#6e8f4a 100%)" role="img" aria-label="Woman jogging outdoors under a blue sky"></div>
      <p class="lorem card-copy">Lorem ipsum dolor sit amet, consec­tetuer adipiscing elit, sed diam non­ummy nibh euismod tincidunt ut laoreet dolore magna aliquam erat volutpat.duis dolore te feugait nulla facilisi.</p>
    </article>
    <article class="abs card" style="left:18px;top:328px">
      <h3 class="card-title"><i></i>Promotional Video</h3>
      <div class="photo card-photo" style="position:relative;background:linear-gradient(135deg,#1f6b2a 0%,#3c9a3a 45%,#2a2a2a 100%)" role="img" aria-label="Presenter filmed in front of a green screen"></div>
      <p class="lorem card-copy">Lorem ipsum dolor sit amet, consec­tetuer adipiscing elit, sed diam non­ummy nibh euismod tincidunt ut laoreet dolore magna aliquam erat volutpat.duis dolore te feugait nulla facilisi.</p>
    </article>
    <article class="abs card" style="left:242px;top:328px">
      <h3 class="card-title"><i></i>Animated Video</h3>
      <div class="photo card-photo" style="position:relative;background:linear-gradient(180deg,#f4f1ea 0%,#f0b6a2 55%,#6fb7d6 100%)" role="img" aria-label="Flat illustrated city skyline"></div>
      <p class="lorem card-copy">Lorem ipsum dolor sit amet, consec­tetuer adipiscing elit, sed diam non­ummy nibh euismod tincidunt ut laoreet dolore magna aliquam erat volutpat.duis dolore te feugait nulla facilisi.</p>
    </article>
  </div>

  <div class="panel why">
    <div class="photo" style="left:13px;top:16px;width:195px;height:208px;background:linear-gradient(135deg,#e9e6e1 0%,#c9b8a2 45%,#5d5852 80%,#2a2a2a 100%)" role="img" aria-label="Film crew with a camera operator and a clapperboard"></div>
    <h2 class="abs heading-blue why-title">Why we are different?</h2>
    <p class="abs lorem why-copy" style="top:275px">Lorem ipsum dolor sit amet, consectetuer adipiscing elit, sed diam nonummy nibh euismod tincidunt ut laoreet dolore magna aliquam erat volutpat. Ut wisi enim ad minim veniam, quis nostrud exerci tation ullamcorper suscipit lobortis­praesent luptatum zzril delenit augue duis dolore te feugait nulla facilisi.</p>
    <p class="abs lorem why-copy" style="top:396px">Lorem ipsum dolor sit amet, consectetuer adipiscing elit, sed diam nonummy nibh euismod tincidunt ut laoreet dolore magna aliquam erat volutpat. Ut wisi enim ad minim veniam, quis nostrud exerci tation ullamcorper suscipit lobortis nisl ut aliquip ex ea commodo consequat. Duis autem vel eum iriure dolor inaugue duis dolore te feugait nulla facilisi.</p>
  </div>
</section>

</body>
</html>
```